Velmora Business Card

We need a design for business cards for our new company. We are a resident safety and security company company that focuses on senior living communities. we provide Nurse call, Access control, CCTV, Wired and wireless network infrastructure, Wander Management, and much more!

Our logo is the circuit board shield. Representing our high tech security solutions. I would like the business card to bring the same theme with perhaps some circuit board traces around the card similar to our logo

```html
<!DOCTYPE html>
<html lang="en">
<head>
<meta charset="utf-8">
<title>Velmora Business Card</title>
<link rel="stylesheet" href="https://fonts.googleapis.com/css2?family=Montserrat:wght@400;700&display=swap">
<style>
  :root {
    --bg: #ecedf0;
    --card: #ffffff;
    --card-shade: #e9eaec;
    --brand-blue: #2f57b0;
    --deep-blue: #2447a3;
    --sky-blue: #5fb4e8;
    --trace-blue: #c9dcf2;
    --ink: #1b1c22;
  }
  * { box-sizing: border-box; margin: 0; padding: 0; }
  html, body { width: 1200px; height: 900px; overflow: hidden; }
  body {
    background: var(--bg);
    font-family: "Montserrat", sans-serif;
    position: relative;
  }
  .card {
    position: absolute;
    left: 250px;
    width: 700px;
    height: 400px;
    border-radius: 22px;
    overflow: hidden;
    box-shadow: 0 10px 30px rgba(0,0,0,.18);
  }
  /* Front */
  .card-front { top: 40px; background: var(--card); }
  .trace-field {
    position: absolute;
    top: 0; bottom: 0;
    width: 260px;
  }
  .trace-field-left {
    left: 0;
    background: linear-gradient(90deg, var(--trace-blue) 0%, rgba(201,220,242,.35) 55%, rgba(255,255,255,0) 100%);
  }
  .trace-field-right {
    right: 0;
    background: linear-gradient(270deg, var(--trace-blue) 0%, rgba(201,220,242,.35) 55%, rgba(255,255,255,0) 100%);
  }
  .front-brand {
    position: absolute;
    inset: 0;
    display: flex;
    align-items: center;
    justify-content: center;
    gap: 18px;
  }
  .brand-dot {
    width: 42px; height: 42px;
    border-radius: 50%;
    background: var(--brand-blue);
  }
  .brand-name {
    font-family: "Montserrat", sans-serif;
    font-weight: 700;
    color: var(--brand-blue);
  }
  .front-brand .brand-name { font-size: 54px; }

  /* Back */
  .card-back {
    top: 470px;
    background: linear-gradient(180deg, var(--card-shade) 0%, var(--card) 70%);
  }
  .back-band {
    position: absolute;
    left: 0; right: 0; bottom: 0;
    height: 24px;
    background: var(--deep-blue);
  }
  .back-feature {
    position: absolute;
    left: 0; top: 40px; bottom: 24px;
    width: 300px;
    background: linear-gradient(160deg, var(--sky-blue) 0%, var(--brand-blue) 100%);
    border-radius: 0 0 150px 0;
  }
  .back-brand {
    position: absolute;
    top: 40px; right: 44px;
  }
  .back-brand .brand-name { font-size: 36px; }
  .contact {
    position: absolute;
    left: 345px; top: 150px;
  }
  .contact-name {
    font-weight: 700;
    font-size: 27px;
    color: var(--brand-blue);
    letter-spacing: .5px;
  }
  .contact-role {
    font-size: 18px;
    color: var(--ink);
    margin: 2px 0 14px;
  }
  .contact-list { list-style: none; }
  .contact-list li {
    display: flex;
    align-items: center;
    gap: 12px;
    font-size: 19px;
    color: var(--ink);
    line-height: 28px;
  }
  .contact-list svg { width: 16px; height: 16px; fill: var(--ink); flex: none; }
</style>
</head>
<body>

<section class="card card-front" aria-label="Card front">
  <div class="trace-field trace-field-left" role="img" aria-label="Light blue circuit board traces"></div>
  <div class="trace-field trace-field-right" role="img" aria-label="Light blue circuit board traces"></div>
  <div class="front-brand">
    <span class="brand-dot"></span>
    <span class="brand-name">Velmora</span>
  </div>
</section>

<section class="card card-back" aria-label="Card back">
  <div class="back-feature" role="img" aria-label="Large blue circuit board graphic"></div>
  <div class="back-brand"><span class="brand-name">Velmora</span></div>
  <div class="contact">
    <p class="contact-name">OWEN MARLICK</p>
    <p class="contact-role">President</p>
    <ul class="contact-list">
      <li>
        <svg viewBox="0 0 16 16"><path d="M3.6 1.5l2.3 2.6-1.3 1.8c.9 2 2.6 3.7 4.6 4.6l1.8-1.3 2.6 2.3-1.5 2.2C6.9 14 2 9.1 1.4 3z"/></svg>
        (555) 214-3870
      </li>
      <li>
        <svg viewBox="0 0 16 16"><path d="M4 1h8v14H4zM5.5 2.5v9.5h5V2.5zM7.2 13h1.6v1H7.2z" fill-rule="evenodd"/></svg>
        (555) 318-4426
      </li>
      <li>
        <svg viewBox="0 0 16 16"><path d="M1 3h14v10H1zM2.5 4.3l5.5 4.4 5.5-4.4v-.3h-11z"/></svg>
        Owen@Velmora.com
      </li>
      <li>
        <svg viewBox="0 0 16 16"><path d="M8 1a7 7 0 1 0 0 14A7 7 0 0 0 8 1zm0 1.5c.8 0 1.7 1.4 2 3.8H6c.3-2.4 1.2-3.8 2-3.8zM2.6 7.3h2.9v1.4H2.6zm7.9 0h2.9v1.4h-2.9zM6 9.7h4c-.3 2.4-1.2 3.8-2 3.8s-1.7-1.4-2-3.8zm0-2.4h4v1.4H6z"/></svg>
        www.Velmora.com
      </li>
    </ul>
  </div>
  <div class="back-band"></div>
</section>

</body>
</html>
```